hotel's Website

Hotels website redesign for reference pictures, logo etc see http://restwellharbourside.co.uk/

1. 2-3 Special offers on the main page.
2. Booking calender
3. Location Map
4. Picture gallery.
5. Journeyrater reviews.
6. short description
7. Social Media sharing.
8 Phone number and address.

Industry/Entity Type

Hotel

Requirements
Must have
• 1. 2-3 Special offers on the main page.
2. Booking calender
3. Location Map
4. Picture gallery.
5. Journeyrater reviews.
6. short description
7. Social Media sharing.

```html
<!DOCTYPE html>
<html lang="en">
<head>
<meta charset="utf-8">
<title>Restwell Hotel – Harbourside</title>
<link href="https://fonts.googleapis.com/css2?family=Cabin:wght@400;500;600&display=swap" rel="stylesheet">
<style>
:root{
  --backdrop:#62a8d9;
  --brand:#0a72c4;
  --brand-dark:#0a5fa8;
  --accent:#ef7a2e;
  --page:#f4f4f4;
  --card:#ffffff;
  --line:#dcdcdc;
  --text:#2e2e2e;
  --muted:#6a6a6a;
  --foot-nav:#262626;
  --foot:#353535;
  --foot-text:#6e6e6e;
  --white:#ffffff;
}
*{box-sizing:border-box;margin:0;padding:0}
html,body{width:680px;height:1200px;overflow:hidden}
body{background:var(--backdrop);font-family:"Cabin",sans-serif;color:var(--text);position:relative}
.site{position:absolute;left:52px;top:80px;width:572px;height:1040px;background:var(--page);overflow:hidden}
.abs{position:absolute}

/* header */
.topbar{left:0;top:0;width:572px;height:36px;background:var(--brand)}
.main-nav{left:148px;top:0;height:36px;display:flex;gap:15px;align-items:center;font-size:7px;color:var(--white)}
.main-nav a{color:var(--white);text-decoration:none;padding:3px 0}
.main-nav a.current{border-bottom:1px solid var(--white)}
.brand{left:76px;top:0;width:56px;height:62px;background:var(--brand-dark);z-index:3;display:flex;flex-direction:column;align-items:center;justify-content:center;gap:4px}
.brand-dot{width:22px;height:22px;border-radius:50%;background:var(--accent)}
.brand-name{font-size:9px;font-weight:500;color:var(--white)}
.brand-group{left:64px;top:67px;font-size:5px;letter-spacing:1.6px;color:var(--white);z-index:3}

/* hero */
.hero{left:0;top:36px;width:572px;height:264px;background:linear-gradient(180deg,#1a1747 0%,#2c2a6a 35%,#3a4c8a 55%,#1c3a6c 75%,#0e1d3a 100%)}
.hero-place{right:18px;top:10px;font-size:6px;color:var(--white)}
.hero-title{left:0;width:572px;top:66px;text-align:center;font-size:24px;font-weight:400;color:var(--white);letter-spacing:.5px}
.booking{left:163px;top:109px;width:232px;height:26px;background:var(--brand);display:flex;align-items:center;justify-content:center;gap:5px;font-size:10px;color:var(--white)}
.booking .field{width:68px;height:10px;background:var(--white)}
.booking .to{margin-left:6px}
.search-btn{left:245px;top:171px;width:85px;height:26px;background:var(--accent);color:var(--white);font-size:7.5px;display:flex;align-items:center;justify-content:center}

/* sections */
.section-title{left:76px;font-size:14px;font-weight:600;color:var(--brand)}
.offers-title{top:325px}
.offer{top:367px;width:135px;height:191px;background:var(--card);border:1px solid var(--line)}
.offer-photo{height:88px;border-bottom:2px solid var(--brand)}
.offer h3{font-size:8px;font-weight:500;margin:11px 0 0 5px}
.offer p{font-size:5.3px;line-height:8px;color:var(--muted);margin:6px 5px 0 5px}
.offer .more{position:absolute;left:5px;bottom:12px;font-size:5.3px;color:var(--brand)}
.o1{left:76px}.o2{left:219px}.o3{left:363px}
.ph1{background:linear-gradient(135deg,#c9b8a8,#e6d23a 45%,#d4415f 80%)}
.ph2{background:linear-gradient(135deg,#9b7b57,#d6a27a 50%,#7a4a2c)}
.ph3{background:linear-gradient(135deg,#d9c4a6,#b73a4a 55%,#8a2e36)}

.location-title{top:584px}
.location{left:76px;top:625px;width:421px;height:148px;background:var(--card);border:1px solid var(--line)}
.map{left:0;top:0;width:277px;height:146px;background:linear-gradient(135deg,#ece6d8,#f3efe6 50%,#e3dccb)}
.contact{left:277px;top:0;width:143px;height:146px;border-left:2px solid var(--brand);padding:10px 0 0 12px}
.contact h4{font-size:8px;font-weight:600;color:var(--brand)}
.contact address{font-style:normal;font-size:5.3px;line-height:8.8px;color:var(--muted);margin-top:4px}
.contact .follow{margin-top:9px}
.socials{display:flex;gap:2px;margin-top:6px}
.socials span{width:11px;height:11px}
.s1{background:#3a3a3a}.s2{background:#3b5998}.s3{background:#35a8e0}.s4{background:#c8232c}.s5{background:#6a9a46}
.signup{display:flex;margin-top:8px}
.signup .email{width:76px;height:15px;border:1px solid var(--line);font-size:5.3px;color:var(--muted);padding:4px 0 0 4px}
.signup .go{width:45px;height:15px;background:var(--brand);color:var(--white);font-size:5.8px;display:flex;align-items:center;justify-content:center}

/* footer */
.foot-nav{left:0;top:845px;width:572px;height:25px;background:var(--foot-nav);display:flex;justify-content:center;align-items:center;gap:15px;font-size:6px;color:#a8a8a8}
.footer{left:0;top:870px;width:572px;height:170px;background:var(--foot)}
.foot-about{left:76px;top:22px;width:128px;font-size:5.3px;line-height:8.6px;color:var(--foot-text)}
.foot-about ul{list-style:none;margin-top:9px}
.partner{left:240px;top:22px;display:flex;align-items:center;gap:6px;font-size:15px;color:var(--white)}
.partner-dot{width:14px;height:14px;border-radius:50%;background:var(--white)}
.foot-rights{right:72px;top:22px;font-size:5.3px;color:var(--foot-text);text-align:right}
</style>
</head>
<body>
<main class="site">
  <header>
    <div class="abs topbar"></div>
    <div class="abs brand"><span class="brand-dot"></span><span class="brand-name">Restwell</span></div>
    <div class="abs brand-group">BY HARBOURLINE HOTELS</div>
    <nav class="abs main-nav">
      <a class="current">Home</a><a>Our rooms</a><a>Atractions</a><a>London Events</a><a>Special Offers</a><a>Photos</a><a>Directions</a><a>Contact</a>
    </nav>
  </header>

  <section class="abs hero" role="img" aria-label="Night view of the river with lit city skyline and bridge">
    <div class="abs hero-place">Harbourside - Quay</div>
    <h1 class="abs hero-title">BOOK A ROOM</h1>
    <div class="abs booking"><span>From</span><span class="field"></span><span class="to">To</span><span class="field"></span></div>
    <div class="abs search-btn">Search Availbility</div>
  </section>

  <h2 class="abs section-title offers-title">Special Offers</h2>
  <article class="abs offer o1">
    <div class="offer-photo ph1" role="img" aria-label="Colourful hotel lounge with yellow armchair"></div>
    <h3>Special offer one</h3>
    <p>Lorem ipsum dolor sit amet, consectetur adipiscing elit. Integer mattis semper nibh vitae euismod. Curabitur rhoncus commodo justo eu luctus. Nulla vulputate egestas lacus, sit amet malesuad.</p>
    <a class="more">Read more</a>
  </article>
  <article class="abs offer o2">
    <div class="offer-photo ph2" role="img" aria-label="Hotel breakfast room with wooden tables"></div>
    <h3>Special offer two</h3>
    <p>Lorem ipsum dolor sit amet, consectetur adipiscing elit. Integer mattis semper nibh vitae euismod. Curabitur rhoncus commodo justo eu luctus. Nulla vulputate egestas lacus, sit amet malesuad.</p>
    <a class="more">Read more</a>
  </article>
  <article class="abs offer o3">
    <div class="offer-photo ph3" role="img" aria-label="Hotel bedroom with red bedspread"></div>
    <h3>Special offer three</h3>
    <p>Lorem ipsum dolor sit amet, consectetur adipiscing elit. Integer mattis semper nibh vitae euismod. Curabitur rhoncus commodo justo eu luctus. Nulla vulputate egestas lacus, sit amet malesuad.</p>
    <a class="more">Read more</a>
  </article>

  <h2 class="abs section-title location-title">Location</h2>
  <section class="abs location">
    <div class="abs map" role="img" aria-label="Street map around the hotel with location pin"></div>
    <div class="abs contact">
      <h4>Contact</h4>
      <address>12-16 Marlow Quay Harbourside<br>HB1 4QA<br>stay@restwellharbourside.co.uk<br>Tel: +44(0) 20 7946 0123<br>Fax: +44(0) 20 7946 0456</address>
      <h4 class="follow">Follow us</h4>
      <div class="socials"><span class="s1"></span><span class="s2"></span><span class="s3"></span><span class="s4"></span><span class="s5"></span></div>
      <div class="signup"><span class="email">Your email adress</span><span class="go">Sign up</span></div>
    </div>
  </section>

  <nav class="abs foot-nav">
    <a>Home</a><a>Our rooms</a><a>Atractions</a><a>London Events</a><a>Special Offers</a><a>Photos</a><a>Directions</a><a>Contact</a>
  </nav>
  <footer class="abs footer">
    <div class="abs foot-about">
      <p>This hotel is owned and operated by the Quayline Hotel Group, please take a look at some of our other hotels below:</p>
      <ul>
        <li>Lanternhouse Hotel - Canal Lock</li>
        <li>Lanternhouse Express - Elm Court</li>
        <li>Meridian House Hotel</li>
        <li>Simplestay Quayside</li>
        <li>Simplestay Northgate</li>
        <li>Restwell Suites - Kingsgate</li>
      </ul>
    </div>
    <div class="abs partner"><span class="partner-dot"></span><span>Journeyrater</span></div>
    <div class="abs foot-rights">All Rights Reserved © 2013</div>
  </footer>
</main>
</body>
</html>
```